Real Estate Business Cards

Looking for a clean, sharp and professional look for our Real Estate investment Fund that invests in Multi Family Apartment buildings.

Target Market(s)

Real Estate Fund

Industry/Entity Type

Real Estate

Contact Information for Business Card

Company Description: Real Estate Investment Fund
Company Name: RKW Holdings
Name: Marcus Olvane
Cell: (917) 482-0657
Email: marcus@rkwholdings-example.com
Website: www.rkwholdings-example.com
Address: 418, 9th Street, Brooklyn NY 11218

Colors

Designer to choose colors to be used in the design.

Requirements
Nice to have
• Colors to match logo

```html
<!DOCTYPE html>
<html lang="en">
<head>
<meta charset="utf-8">
<title>RKW Holdings — Business Card</title>
<link rel="stylesheet" href="https://fonts.googleapis.com/css2?family=EB+Garamond:wght@400;500;700&display=swap">
<style>
  :root {
    --stage: #e9eaed;
    --navy: #22273a;
    --brand-blue: #0f72ab;
    --ink: #2b2b2b;
    --paper: #ffffff;
  }
  * { box-sizing: border-box; margin: 0; padding: 0; }
  html, body { width: 1200px; height: 1200px; overflow: hidden; }
  body {
    background: var(--stage);
    font-family: "EB Garamond", Georgia, serif;
    position: relative;
  }
  .card {
    position: absolute;
    left: 150px;
    width: 900px;
    height: 514px;
    border-radius: 34px;
    overflow: hidden;
    box-shadow: 0 6px 22px rgba(0,0,0,0.18);
  }
  /* Back side */
  .card-back { top: 66px; background: var(--navy); }
  .back-wordmark {
    position: absolute;
    right: 90px;
    bottom: 90px;
    display: flex;
    align-items: center;
    gap: 18px;
  }
  .wordmark-square {
    width: 34px; height: 34px;
    background: var(--brand-blue);
  }
  .wordmark-name {
    color: var(--brand-blue);
    font-weight: 500;
    font-size: 52px;
    letter-spacing: 2px;
    text-transform: uppercase;
  }
  /* Front side */
  .card-front { top: 620px; background: var(--paper); }
  .front-wordmark {
    position: absolute;
    right: 80px;
    top: 120px;
    display: flex;
    align-items: center;
    gap: 14px;
  }
  .front-wordmark .wordmark-square { width: 28px; height: 28px; }
  .front-wordmark .wordmark-name { font-size: 40px; }
  .holder {
    position: absolute;
    left: 78px;
    top: 222px;
  }
  .holder-name {
    color: var(--brand-blue);
    font-weight: 700;
    font-size: 36px;
    letter-spacing: 1px;
    text-transform: uppercase;
  }
  .holder-company {
    margin-top: 10px;
    color: var(--brand-blue);
    font-weight: 500;
    font-size: 22px;
    text-transform: uppercase;
    letter-spacing: 0.5px;
  }
  .holder-address, .contact-line {
    color: var(--ink);
    font-size: 21px;
    line-height: 1.3;
  }
  .contact-line { display: flex; align-items: center; gap: 8px; }
  .icon { width: 18px; height: 18px; flex: none; }
  .online {
    position: absolute;
    left: 430px;
    top: 356px;
  }
  .footer-band {
    position: absolute;
    left: 0; right: 0; bottom: 0;
    height: 78px;
    background: var(--brand-blue);
    display: flex;
    align-items: center;
    justify-content: center;
    color: var(--paper);
    font-weight: 500;
    font-size: 24px;
    letter-spacing: 2px;
    text-transform: uppercase;
  }
</style>
</head>
<body>
  <section class="card card-back" aria-label="Card back">
    <div class="back-wordmark">
      <span class="wordmark-square"></span>
      <span class="wordmark-name">RKW Holdings</span>
    </div>
  </section>

  <section class="card card-front" aria-label="Card front">
    <div class="front-wordmark">
      <span class="wordmark-square"></span>
      <span class="wordmark-name">RKW Holdings</span>
    </div>

    <div class="holder">
      <h1 class="holder-name">Marcus Olvane</h1>
      <p class="holder-company">RKW Holdings</p>
      <p class="holder-address">418, 9th Street, Brooklyn NY 11218</p>
      <p class="contact-line">
        <svg class="icon" viewBox="0 0 20 20" aria-hidden="true"><circle cx="10" cy="10" r="10" fill="#0f72ab"/><path d="M7 5.5l2 2-1 1.2a6 6 0 0 0 3.3 3.3l1.2-1 2 2-1.3 1.5C9.5 14.5 5.5 10.5 5.5 6.8z" fill="#fff"/></svg>
        (917) 482-0657
      </p>
    </div>

    <div class="online">
      <p class="contact-line">
        <svg class="icon" viewBox="0 0 20 20" aria-hidden="true"><circle cx="10" cy="10" r="10" fill="#0f72ab"/><rect x="5" y="6.5" width="10" height="7" fill="none" stroke="#fff" stroke-width="1.2"/><path d="M5 6.5l5 4 5-4" fill="none" stroke="#fff" stroke-width="1.2"/></svg>
        marcus@rkwholdings-example.com
      </p>
      <p class="contact-line">
        <svg class="icon" viewBox="0 0 20 20" aria-hidden="true"><circle cx="10" cy="10" r="10" fill="#0f72ab"/><circle cx="10" cy="10" r="5.5" fill="none" stroke="#fff" stroke-width="1.1"/><ellipse cx="10" cy="10" rx="2.4" ry="5.5" fill="none" stroke="#fff" stroke-width="1"/><path d="M4.5 10h11" stroke="#fff" stroke-width="1"/></svg>
        www.rkwholdings-example.com
      </p>
    </div>

    <div class="footer-band">Real Estate Investment Fund</div>
  </section>
</body>
</html>
```